Lustra Vale Label

Design a label for the new brand Lustra Vale. The specific product label : Lustra Vale Deep Moisturizing Conditioner.

You only need to design the front label.I have included the logo and a bottle jpeg. Please try your best.

Industry/Entity Type

Product

Requirements
Must have
• text you can use:
• For Dry, Damaged Hair
• Strengthening & Moisturizing Conditioner
• Moisture Infused
• Deep Penetrating Formula
• Used by Professionals
• 8.5oz/250ml

```html
<!DOCTYPE html>
<html lang="en">
<head>
<meta charset="utf-8">
<title>Lustra Vale Deep Moisturizing Conditioner – Front Label</title>
<link rel="stylesheet" href="https://fonts.googleapis.com/css2?family=Roboto+Condensed:wght@700&family=Roboto:wght@400&display=swap">
<style>
  :root {
    --page: #ffffff;
    --sky: #a9dcea;
    --sky-light: #e6f5fa;
    --white: #ffffff;
    --silver: #9a9b9e;
    --yellow: #ffe000;
    --yellow-soft: #ffe94d;
    --gold: #d49b00;
    --ink: #111111;
    --photo-dark: #3b3230;
    --photo-mid: #8a6b55;
    --legend: #222222;
  }
  html, body {
    margin: 0;
    padding: 0;
    width: 1200px;
    height: 1200px;
    overflow: hidden;
    background: var(--page);
  }
  .canvas {
    position: relative;
    width: 1200px;
    height: 1200px;
  }
  .label {
    position: absolute;
    left: 436px;
    top: 50px;
    width: 327px;
    height: 1000px;
    display: block;
  }
  .label-text {
    font-family: "Roboto Condensed", "Arial Narrow", sans-serif;
    font-weight: 700;
    fill: var(--ink);
  }
  .brand-name {
    font-family: "Roboto Condensed", "Arial Narrow", sans-serif;
    font-weight: 700;
    fill: var(--gold);
  }
  .legend {
    position: absolute;
    left: 436px;
    top: 1090px;
    display: flex;
    align-items: center;
    gap: 14px;
    font-family: "Roboto", Arial, sans-serif;
    font-size: 30px;
    color: var(--legend);
  }
  .legend-swatch {
    width: 26px;
    height: 26px;
    background: var(--silver);
  }
</style>
</head>
<body>
<main class="canvas">
  <svg class="label" viewBox="0 0 180 550" xmlns="http://www.w3.org/2000/svg" aria-label="Lustra Vale Deep Moisturizing Conditioner front label">
    <defs>
      <clipPath id="label-shape">
        <rect x="0" y="0" width="180" height="550" rx="8" ry="8"/>
      </clipPath>
      <linearGradient id="sky-fill" x1="0" y1="0" x2="0" y2="1">
        <stop offset="0" stop-color="var(--sky)"/>
        <stop offset="0.7" stop-color="var(--sky)"/>
        <stop offset="1" stop-color="var(--sky-light)"/>
      </linearGradient>
      <linearGradient id="panel-fill" x1="0" y1="0" x2="0" y2="1">
        <stop offset="0" stop-color="var(--white)"/>
        <stop offset="0.55" stop-color="var(--white)"/>
        <stop offset="1" stop-color="var(--sky-light)"/>
      </linearGradient>
      <linearGradient id="bottom-fill" x1="0" y1="0" x2="1" y2="1">
        <stop offset="0" stop-color="var(--sky)"/>
        <stop offset="1" stop-color="var(--sky-light)"/>
      </linearGradient>
      <radialGradient id="photo-fill" cx="0.45" cy="0.4" r="0.7">
        <stop offset="0" stop-color="var(--photo-mid)"/>
        <stop offset="1" stop-color="var(--photo-dark)"/>
      </radialGradient>
    </defs>

    <g clip-path="url(#label-shape)">
      <rect class="label-base" x="0" y="0" width="180" height="550" fill="url(#sky-fill)"/>
      <!-- silver foil sweep -->
      <path class="silver-sweep" d="M0,0 L118,0 C178,70 196,250 168,385 C148,470 70,530 0,552 Z" fill="var(--silver)"/>
      <!-- white main panel -->
      <path class="main-panel" d="M0,0 L110,0 C170,65 186,250 160,382 C140,462 62,522 0,544 Z" fill="url(#panel-fill)"/>
      <!-- light bottom-left fade -->
      <path class="bottom-fade" d="M0,556 L0,548 C70,526 150,468 170,388 L180,400 L180,556 Z" fill="url(#bottom-fill)" opacity="0.0"/>

      <!-- NEW corner -->
      <path class="new-corner" d="M0,0 L62,0 L0,34 Z" fill="var(--yellow)"/>
      <text class="label-text new-tag" x="16" y="28" font-size="12" transform="rotate(-22 16 28)">NEW</text>

      <!-- brand name -->
      <circle class="brand-dot" cx="90" cy="92" r="14" fill="var(--gold)"/>
      <text class="brand-name" x="90" y="150" font-size="27" text-anchor="middle">Lustra Vale</text>

      <!-- product title band -->
      <rect class="title-band" x="0" y="208" width="166" height="50" fill="var(--yellow)"/>
      <text class="label-text" x="83" y="229" font-size="17.5" text-anchor="middle">DEEP</text>
      <text class="label-text" x="83" y="252" font-size="17.5" text-anchor="middle">MOISTURIZING</text>
      <rect class="subtitle-band" x="0" y="262" width="166" height="16" fill="var(--yellow-soft)"/>
      <text class="label-text" x="117" y="274" font-size="9" text-anchor="middle">CONDITIONER</text>

      <!-- model photo -->
      <circle class="photo-ring" cx="99" cy="380" r="77" fill="var(--white)" opacity="0.8"/>
      <circle class="photo-ring" cx="99" cy="380" r="73" fill="var(--yellow)"/>
      <circle class="photo" cx="99" cy="380" r="69" fill="url(#photo-fill)" role="img" aria-label="Photo of a model with long glossy brown hair"/>

      <!-- claims -->
      <text class="label-text" x="138" y="492" font-size="9" text-anchor="middle">SOFTNESS</text>
      <text class="label-text" x="138" y="505" font-size="9" text-anchor="middle">AND SHINE</text>
      <text class="label-text" x="138" y="529" font-size="7" text-anchor="middle">8.5oz/250ml</text>
    </g>
    <rect x="0.25" y="0.25" width="179.5" height="549.5" rx="8" ry="8" fill="none" stroke="#cfd6d9" stroke-width="0.5"/>
  </svg>

  <div class="legend">
    <span class="legend-swatch"></span>
    <span class="legend-text">Silver Foiling Area</span>
  </div>
</main>
</body>
</html>
```